Please create a custom stationary design for Lantor reporting. The logo is attached to this brief.
I need more time thanks
Reason: I need to update my logo. Sorry, it was wrong one.
Please provide STATIONERY DESIGN, Not only Business cards.
Some of you only post business card.
Could you add datavisualization charts filigrams please.
Heat map, relation circle, tree map, staked bar chart, Gauge chart, line chart region.
Not to much but clean and beautifull.
http://qelbix.org/examples.html
http://www.morvadi.com/15523-clean-vector-infographic-and-data-visualization-design-elements-03/
http://plotrune.ch/notes/tilcards/

```html
<!DOCTYPE html>
<html lang="en">
<head>
<meta charset="utf-8">
<title>Lantor reporting – Stationery</title>
<link rel="stylesheet" href="https://fonts.googleapis.com/css2?family=Open+Sans:wght@400;600&display=swap">
<style>
  :root {
    --bg: #2b2b2d;
    --paper: #ffffff;
    --brand-blue: #1a8fd8;
    --deep-blue: #1569b8;
    --ink: #2c2c2c;
    --muted: #555555;
    --rule: #c8c8c8;
    --band: #1f7fcc;
  }
  * { box-sizing: border-box; margin: 0; padding: 0; }
  html, body { width: 1200px; height: 1000px; overflow: hidden; }
  body { background: var(--bg); position: relative; font-family: "Open Sans", Arial, sans-serif; color: var(--ink); }

  .sheet { position: absolute; background: var(--paper); box-shadow: 0 10px 30px rgba(0,0,0,.45); overflow: hidden; }

  .brand { display: flex; align-items: center; gap: 10px; font-family: "Open Sans", Arial, sans-serif; font-weight: 400; color: var(--brand-blue); white-space: nowrap; line-height: 1; }
  .brand-mark { background: var(--brand-blue); flex: none; }

  .footer-band { position: absolute; left: 0; right: 0; bottom: 0; background: var(--band); }

  /* Envelope */
  .envelope { left: 60px; top: 80px; width: 600px; height: 300px; }
  .envelope .brand { position: absolute; left: 28px; top: 28px; font-size: 20px; }
  .envelope .brand-mark { width: 20px; height: 20px; }
  .envelope .address { position: absolute; right: 26px; bottom: 18px; font-size: 11px; font-weight: 600; }
  .envelope .footer-band { height: 4px; }

  /* Business card front */
  .card-front { left: 60px; top: 430px; width: 400px; height: 230px; }
  .card-front .brand { position: absolute; left: 40px; top: 40px; font-size: 28px; }
  .card-front .brand-mark { width: 28px; height: 28px; }
  .card-front .person { position: absolute; left: 40px; top: 126px; }
  .card-front .person-name { font-weight: 400; color: var(--brand-blue); font-size: 17px; line-height: 1.2; }
  .card-front .person-role { font-size: 11px; color: var(--muted); margin-top: 2px; }
  .card-front .divider { position: absolute; left: 172px; top: 124px; width: 1px; height: 70px; background: var(--rule); }
  .card-front .contact { position: absolute; left: 186px; top: 122px; list-style: none; font-size: 11px; font-weight: 600; line-height: 17px; }
  .contact li { display: flex; align-items: center; gap: 6px; }
  .contact li.no-icon { padding-left: 16px; }
  .contact svg { width: 10px; height: 10px; flex: none; }
  .card-front .footer-band { height: 5px; }

  /* Business card back */
  .card-back { left: 60px; top: 700px; width: 400px; height: 230px; background: linear-gradient(135deg, var(--deep-blue), var(--brand-blue)); }
  .card-back .brand { position: absolute; left: 50%; top: 50%; transform: translate(-50%, -50%); font-size: 26px; color: var(--paper); }
  .card-back .brand-mark { width: 26px; height: 26px; background: var(--paper); }

  /* Letterhead */
  .letterhead { left: 720px; top: 170px; width: 440px; height: 622px; }
  .letterhead .brand { position: absolute; left: 50%; transform: translateX(-50%); top: 40px; font-size: 22px; }
  .letterhead .brand-mark { width: 22px; height: 22px; }
  .letterhead .footer { position: absolute; right: 24px; bottom: 18px; text-align: right; font-size: 8px; }
  .letterhead .footer .address { margin-bottom: 4px; }
  .letterhead .footer .contact-row { display: flex; gap: 10px; justify-content: flex-end; align-items: center; }
  .letterhead .footer .contact-row span { display: flex; align-items: center; gap: 3px; }
  .letterhead .footer svg { width: 8px; height: 8px; }
  .letterhead .footer-band { height: 4px; }
</style>
</head>
<body>

  <section class="sheet envelope" aria-label="Envelope">
    <div class="brand"><span class="brand-mark"></span>Lantor reporting</div>
    <p class="address">64/20 Halden Street, Tamara</p>
    <div class="footer-band"></div>
  </section>

  <section class="sheet card-front" aria-label="Business card front">
    <div class="brand"><span class="brand-mark"></span>Lantor reporting</div>
    <div class="person">
      <p class="person-name">Marek Dolan</p>
      <p class="person-role">CEO</p>
    </div>
    <div class="divider"></div>
    <ul class="contact">
      <li class="no-icon">64/20 Halden Street, Tamara</li>
      <li><svg viewBox="0 0 10 10"><path d="M2 1 L4 1 L4.6 3 L3.4 4 Q4.5 6 6 6.6 L7 5.4 L9 6 L9 8 Q5 9 1 2 Z" fill="var(--brand-blue)"/></svg>+1 555 018 2046</li>
      <li><svg viewBox="0 0 10 10"><rect x="0.5" y="2" width="9" height="6" fill="none" stroke="var(--brand-blue)"/><path d="M0.5 2 L5 5.5 L9.5 2" fill="none" stroke="var(--brand-blue)"/></svg>info@lantorreporting.com</li>
      <li><svg viewBox="0 0 10 10"><circle cx="5" cy="5" r="4.3" fill="none" stroke="var(--brand-blue)"/><path d="M0.7 5 H9.3 M5 0.7 Q2.5 5 5 9.3 M5 0.7 Q7.5 5 5 9.3" fill="none" stroke="var(--brand-blue)" stroke-width="0.8"/></svg>www.lantorreporting.com</li>
    </ul>
    <div class="footer-band"></div>
  </section>

  <section class="sheet card-back" aria-label="Business card back">
    <div class="brand"><span class="brand-mark"></span>Lantor reporting</div>
  </section>

  <section class="sheet letterhead" aria-label="Letterhead">
    <div class="brand"><span class="brand-mark"></span>Lantor reporting</div>
    <div class="footer">
      <p class="address">64/20 Halden Street, Tamara</p>
      <div class="contact-row">
        <span><svg viewBox="0 0 10 10"><path d="M2 1 L4 1 L4.6 3 L3.4 4 Q4.5 6 6 6.6 L7 5.4 L9 6 L9 8 Q5 9 1 2 Z" fill="var(--brand-blue)"/></svg>+1 555 018 2046</span>
        <span><svg viewBox="0 0 10 10"><rect x="0.5" y="2" width="9" height="6" fill="none" stroke="var(--brand-blue)"/><path d="M0.5 2 L5 5.5 L9.5 2" fill="none" stroke="var(--brand-blue)"/></svg>info@lantorreporting.com</span>
        <span><svg viewBox="0 0 10 10"><circle cx="5" cy="5" r="4.3" fill="none" stroke="var(--brand-blue)"/><path d="M0.7 5 H9.3 M5 0.7 Q2.5 5 5 9.3 M5 0.7 Q7.5 5 5 9.3" fill="none" stroke="var(--brand-blue)" stroke-width="0.8"/></svg>www.lantorreporting.com</span>
      </div>
    </div>
    <div class="footer-band"></div>
  </section>

</body>
</html>
```